Ecommerce site that acts also as a portal for B2C members and non- members and B2B. Please see attachment this is for only front end work, backend will follow. Brew and Mill- a KRWE Hospitality Company

Products
Coffee bean sourcing, acquisition, roasting, grinding, blending, sale/delivery
Tea sourcing, acquisition, roasting, grinding, blending, sale/delivery
Applicable/Associated Merchandise and Accoutrements

Initial market penetration for both B2C and B2B offering Brew and Mill custom blends of both Coffees and Teas.
B2C- Zolvex style sale/distribution via guest and members. Members initial fee $129 annual $99 a year thereafter with benefits such as 1st year gift of a French Press Travel Mug (customized/logo/name/brand), monthly samples. Attached document has non project related information for narrative and conceptual inputs.

```html
<!DOCTYPE html>
<html lang="en">
<head>
<meta charset="utf-8">
<title>Brew and Mill — Luxury Coffee &amp; Tea</title>
<link href="https://fonts.googleapis.com/css2?family=Playfair+Display:wght@400;700&family=Mulish:ital,wght@0,400;0,600;0,700;1,400&display=swap" rel="stylesheet">
<style>
:root{
  --gold:#f2b84b;
  --gold-line:#e9b457;
  --btn:#8b4f1b;
  --btn-text:#f3d9b8;
  --nav-active:#e38a3a;
  --brand:#c8935a;
  --text:#ffffff;
  --card-light:#e7e6e5;
  --card-dark:#121110;
  --ink:#2a221d;
}
*{margin:0;padding:0;box-sizing:border-box}
html,body{width:1200px;height:4451px;overflow:hidden}
body{
  position:relative;
  font-family:'Mulish',sans-serif;color:var(--text);
  background:
    linear-gradient(180deg,
      #2a1a10 0px,#24160d 560px,#2b190e 1150px,#241509 1700px,
      #0e0b09 1850px,#0d0b0a 2420px,
      #2a180c 2480px,#26160c 2950px,
      #0d0b0a 3000px,#0d0b0a 3600px,
      #1d130c 3680px,#150e09 4451px);
}
.abs{position:absolute}
.serif{font-family:'Playfair Display',serif}
.gold{color:var(--gold)}
.btn{position:absolute;display:flex;align-items:center;justify-content:center;border-radius:24px;font-size:12px;font-weight:600;color:var(--btn-text);background:var(--btn)}
.btn.outline{background:transparent;border:2px solid #fff;color:#fff}

/* header */
.brand-name{left:150px;top:42px;font-family:'Playfair Display',serif;font-size:22px;font-weight:400;color:var(--brand)}
.nav a{position:absolute;top:47px;font-size:13px;color:#fff;text-decoration:none}
.nav a.active{color:var(--nav-active)}
.icon{position:absolute;top:44px}

/* hero */
.hero-title{left:150px;top:210px;font-size:60px;line-height:67px;font-weight:400}
.hero-title b{font-weight:700}
.hero-sub{left:150px;top:357px;width:460px;font-size:12.5px;line-height:18px}
.cup{position:absolute;left:672px;top:128px;width:430px;height:380px;border-radius:50%;background:radial-gradient(circle at 45% 50%,#c99566 0 18%,#6b3b1c 30%,#8c7a6a 44%,#4a3a2f 58%,transparent 68%)}

/* framed images */
.framed{position:absolute;border-radius:46px;overflow:hidden}
.frame-line{position:absolute;border:4px solid var(--gold-line);border-radius:50px}
.h2{font-family:'Playfair Display',serif;font-size:38px;line-height:48px;font-weight:400}
.h2 strong{font-weight:700;color:var(--gold)}
.body-copy{font-size:15px;line-height:26px;text-align:justify}
.checks{list-style:none}
.checks li{display:flex;align-items:center;gap:14px;font-size:14px;line-height:26px}
.checks b{color:var(--gold);font-weight:700}
.tray{position:absolute;background:linear-gradient(135deg,#3a2414,#5a3517 50%,#1e2a14);transform:rotate(35deg);border-radius:8px;opacity:.9}

.center{position:absolute;left:0;width:1200px;text-align:center}
.section-sub{font-size:14px}

/* cards */
.card{position:absolute;width:287px;border-radius:16px;overflow:hidden}
.card.light{background:var(--card-light);color:var(--ink)}
.card.dark{background:var(--card-dark);color:#fff}
.card .img{width:100%}
.card h3{font-family:'Playfair Display',serif;font-size:16px;font-weight:700;margin:20px 26px 10px}
.card p{font-size:12px;line-height:22px;margin:0 26px}
.card .price{font-size:26px;font-weight:700;margin:8px 26px 0}

/* membership */
.benefits{left:150px;top:2647px;width:422px;height:242px;border-radius:34px;background:#0f0c0a;padding:28px 28px}
.benefits h3{font-family:'Playfair Display',serif;font-size:18px;margin-bottom:20px}
.benefits li{font-size:12.5px;line-height:34px}

/* newsletter */
.news-arc{left:152px;top:3679px;width:896px;height:90px;border:5px solid var(--gold-line);border-bottom:none;border-radius:40px 40px 0 0}

/* footer */
.footer-brand{top:4110px;font-family:'Playfair Display',serif;font-size:40px;font-weight:400;color:#fff}
.foot-links a{position:absolute;top:4236px;font-size:16px;color:#fff;text-decoration:none}
.rule{left:150px;top:4369px;width:900px;height:1px;background:#4a3b30}
</style>
</head>
<body>

<!-- header -->
<div class="abs brand-name">Brew and Mill</div>
<nav class="nav">
  <a class="active" style="left:367px">Home</a>
  <a style="left:440px">About Us</a>
  <a style="left:533px">Wholesale</a>
  <a style="left:634px">Collections</a>
  <a style="left:736px">Membership</a>
  <a style="left:849px">Contact</a>
</nav>
<svg class="icon" style="left:934px" width="22" height="22" viewBox="0 0 22 22" fill="none" stroke="#fff" stroke-width="2.2"><circle cx="9" cy="9" r="7"/><path d="M14 14l6 6"/></svg>
<svg class="icon" style="left:980px" width="28" height="26" viewBox="0 0 28 26" fill="none"><path d="M11 23C4 17 2 13 2 9a5 5 0 0 1 9-3 5 5 0 0 1 9 3c0 4-2 8-9 14z" stroke="#fff" stroke-width="2"/><circle cx="21" cy="5" r="5" fill="#fff"/><text x="21" y="8" font-size="8" text-anchor="middle" fill="#000" font-family="Mulish,sans-serif">0</text></svg>
<svg class="icon" style="left:1029px" width="18" height="20" viewBox="0 0 18 20" fill="none" stroke="#fff" stroke-width="2"><path d="M2 7h14l-1 12H3z"/><path d="M6 7V5a3 3 0 0 1 6 0v2"/></svg>

<!-- hero -->
<div class="cup" role="img" aria-label="Cup of latte with leaf latte art seen from above, coffee beans around"></div>
<h1 class="abs hero-title serif"><b>Luxury Coffee &amp;<br>Tea,</b> Crafted by You.</h1>
<p class="abs hero-sub">Custom-blended coffees and teas sourced from the world's most respected origins—roasted, blended, and delivered fresh to your door.</p>
<a class="btn" style="left:150px;top:418px;width:146px;height:44px">Build Your Blend</a>
<a class="btn outline" style="left:318px;top:418px;width:164px;height:44px">Shop the Collection</a>

<!-- crafted -->
<div class="tray" style="left:-30px;top:850px;width:260px;height:230px" role="img" aria-label="Wooden tray with a cup of tea and green leaves"></div>
<div class="frame-line" style="left:144px;top:597px;width:434px;height:449px"></div>
<div class="framed" style="left:152px;top:603px;width:424px;height:443px;background:linear-gradient(180deg,#3b2718,#6a4628 45%,#2a1a10)" role="img" aria-label="Dining room with curved wooden slat ceiling and cream chairs"></div>
<h2 class="abs h2" style="left:626px;top:620px">Crafted With Intention.<br><strong>Delivered With Precision.</strong></h2>
<p class="abs body-copy" style="left:629px;top:742px;width:417px">Every cup begins with exceptional raw materials, ethical sourcing, and obsessive attention to detail. At Brew &amp; Mill, we bring together the art of blending and the science of roasting to create a truly personalized coffee and tea experience.</p>
<ul class="abs checks" style="left:636px;top:902px">
  <li><svg width="14" height="14" viewBox="0 0 14 14"><circle cx="7" cy="7" r="7" fill="#f2b84b"/><path d="M4 7l2 2 4-4" stroke="#140c08" stroke-width="1.8" fill="none"/></svg><span><b>Source</b> – Direct relationships with world-class growers</span></li>
  <li><svg width="14" height="14" viewBox="0 0 14 14"><circle cx="7" cy="7" r="7" fill="#f2b84b"/><path d="M4 7l2 2 4-4" stroke="#140c08" stroke-width="1.8" fill="none"/></svg><span><b>Blend</b> – Customize flavor, body, and aroma</span></li>
  <li><svg width="14" height="14" viewBox="0 0 14 14"><circle cx="7" cy="7" r="7" fill="#f2b84b"/><path d="M4 7l2 2 4-4" stroke="#140c08" stroke-width="1.8" fill="none"/></svg><span><b>Roast</b> – Small-batch precision for peak freshness</span></li>
  <li><svg width="14" height="14" viewBox="0 0 14 14"><circle cx="7" cy="7" r="7" fill="#f2b84b"/><path d="M4 7l2 2 4-4" stroke="#140c08" stroke-width="1.8" fill="none"/></svg><span><b>Deliver</b> – Sealed, protected, and shipped fast</span></li>
</ul>

<!-- featured collections -->
<h2 class="center h2" style="top:1196px">Featured <strong>Collections</strong></h2>
<p class="center section-sub" style="top:1258px">From single-origin purity to fully customized blends, discover our curated collections</p>
<div class="card light" style="left:150px;top:1326px;height:320px"><div class="img" style="height:208px;background:linear-gradient(180deg,#5a4a40,#3a2012 50%,#1a0e08)" role="img" aria-label="Roasted coffee beans in a roasting drum"></div><h3>Single-Origin Coffees</h3><p>Pure expressions of place, terroir, and craft.</p></div>
<div class="card dark" style="left:456px;top:1326px;height:320px"><div class="img" style="height:208px;background:linear-gradient(180deg,#1a0f09,#5a301a 55%,#8a4a26)" role="img" aria-label="Coffee beans falling onto a pile of ground coffee"></div><h3>Custom Coffee Blends</h3><p>Design your own blend—your flavor profile, your name, your ritual.</p></div>
<div class="card light" style="left:762px;top:1326px;height:320px"><div class="img" style="height:208px;background:linear-gradient(180deg,#3a2a1e,#5a4a2c 55%,#7a4a22)" role="img" aria-label="Clay teapot, loose tea leaves and a glass of tea"></div><h3>Artisan Teas</h3><p>Whole-leaf teas and botanical blends, sourced seasonally and blended with</p></div>
<a class="btn" style="left:507px;top:1700px;width:186px;height:43px">Shop Coffee | Shop Tea</a>

<!-- sourced -->
<h2 class="abs h2" style="left:150px;top:1955px">Sourced From the<br><strong>World’s Finest Regions</strong></h2>
<p class="abs body-copy" style="left:152px;top:2078px;width:418px">Great coffee and tea begin at origin. Explore the regions behind every blend—each with its own altitude, climate, processing methods, and flavor signatures.<br>From Ethiopian highlands to Japanese tea gardens, our sourcing is transparent, ethical, and intentional.</p>
<a class="btn" style="left:150px;top:2243px;width:166px;height:43px">Explore Origins</a>
<div class="tray" style="left:1000px;top:2150px;width:250px;height:230px" role="img" aria-label="Wooden tray with a cup of tea and green leaves"></div>
<div class="frame-line" style="left:631px;top:1904px;width:418px;height:435px"></div>
<div class="framed" style="left:631px;top:1904px;width:410px;height:435px;background:linear-gradient(180deg,#2a2622,#5a5048 40%,#7a7068 70%,#1f5a52)" role="img" aria-label="Roastery floor with copper roasting machines"></div>

<!-- membership -->
<h2 class="center h2" style="top:2516px">The Brew &amp; Mill <strong>Membership</strong></h2>
<p class="center section-sub" style="top:2578px">Designed for those who appreciate exclusivity, customization, and discovery.</p>
<div class="abs benefits">
  <h3>Membership Benefits</h3>
  <ul class="checks">
    <li style="font-size:12.5px;line-height:34px"><svg width="12" height="12" viewBox="0 0 14 14"><circle cx="7" cy="7" r="7" fill="#f2b84b"/><path d="M4 7l2 2 4-4" stroke="#140c08" stroke-width="1.8" fill="none"/></svg>Custom French Press Travel Mug (Year One Gift)</li>
    <li style="font-size:12.5px;line-height:34px"><svg width="12" height="12" viewBox="0 0 14 14"><circle cx="7" cy="7" r="7" fill="#f2b84b"/><path d="M4 7l2 2 4-4" stroke="#140c08" stroke-width="1.8" fill="none"/></svg>Monthly coffee or tea samples</li>
    <li style="font-size:12.5px;line-height:34px"><svg width="12" height="12" viewBox="0 0 14 14"><circle cx="7" cy="7" r="7" fill="#f2b84b"/><path d="M4 7l2 2 4-4" stroke="#140c08" stroke-width="1.8" fill="none"/></svg>Expanded blend customization</li>
    <li style="font-size:12.5px;line-height:34px"><svg width="12" height="12" viewBox="0 0 14 14"><circle cx="7" cy="7" r="7" fill="#f2b84b"/><path d="M4 7l2 2 4-4" stroke="#140c08" stroke-width="1.8" fill="none"/></svg>Early access to reserve and seasonal releases</li>
  </ul>
</div>
<h3 class="abs serif" style="left:626px;top:2670px;font-size:18px">Pricing</h3>
<p class="abs serif gold" style="left:628px;top:2710px;font-size:22px;font-weight:700;line-height:34px">$129 First Year<br>$99 Annual Renewal</p>
<a class="btn" style="left:626px;top:2797px;width:166px;height:42px">Become a Member</a>

<!-- featured products -->
<h2 class="center h2" style="top:3016px">Featured <strong>Products</strong></h2>
<p class="center section-sub" style="top:3077px">Discover what our community reaches for again and again—exceptional coffees, refined teas, and thoughtfully designed</p>
<div class="card dark" style="left:150px;top:3145px;height:320px"><div class="img" style="height:209px;background:linear-gradient(180deg,#6a3a18,#2a1a10 55%,#8a5a2a)" role="img" aria-label="Espresso pouring into a glass cup"></div><h3>Small-Batch Roasted Coffees</h3><p class="price">$ 85.00</p></div>
<div class="card light" style="left:456px;top:3145px;height:320px"><div class="img" style="height:209px;background:linear-gradient(180deg,#4a5a2a,#2f4a1a 55%,#5a4a2a)" role="img" aria-label="Baskets of green tea leaves"></div><h3>Whole-Leaf Artisan Teas</h3><p class="price">$ 55.00</p></div>
<div class="card light" style="left:762px;top:3145px;height:320px"><div class="img" style="height:209px;background:linear-gradient(180deg,#3a2418,#c8955a 50%,#6a3a1a)" role="img" aria-label="Two iced blended coffee drinks with cream"></div><h3>Limited Seasonal Blends</h3><p class="price">$ 45.00</p></div>
<a class="btn" style="left:507px;top:3520px;width:186px;height:42px">Shop Coffee | Shop Tea</a>

<!-- newsletter -->
<div class="abs news-arc"></div>
<div class="tray" style="left:-30px;top:3830px;width:250px;height:230px" role="img" aria-label="Wooden tray with a cup of tea and green leaves"></div>
<h2 class="center h2" style="top:3728px">Newsletter <strong>Sign-up</strong></h2>
<p class="center section-sub" style="top:3793px">Be the first to access new releases, seasonal blends, and exclusive offers.</p>
<a class="btn" style="left:531px;top:3847px;width:138px;height:42px">Join the List</a>

<!-- footer -->
<div class="center footer-brand">Brew and Mill</div>
<nav class="foot-links">
  <a style="left:293px">Home</a>
  <a style="left:377px">About Us</a>
  <a style="left:487px">Destinations</a>
  <a style="left:622px">Collections</a>
  <a style="left:743px">Partners</a>
  <a style="left:846px">Contact</a>
</nav>
<p class="center" style="top:4286px;font-size:16px;font-style:italic;line-height:23px">Luxury Coffee &amp; Tea, Crafted by You.<br>A Division of KRWE Hospitality</p>
<div class="abs rule"></div>
<p class="center" style="top:4400px;font-size:16px">Copyright 2026. Company Name. All Rights Reserved</p>

</body>
</html>
```